Concrete Finishing business needs new business card and a logo design

We are a family owned and operated, concrete finishing business. 2020 marks our 33 rd year in business. We operate under Harold M. Ferrick and Sons Concrete Contractors Ltd. Harold M was my father and founder of the company. We usually shorten the name and use H M Ferrick & Sons Ltd. Most people in the Concrete Finishing industry tend to know us by our last name 'Ferrick' . in honour of our father, we would still like to have his name on the cards and logo but are open to shortening it to H.M (maybe in a small font with the W on top of the J ) and focusing more on the "Ferrick & Sons."....Or maybe something with just the initials HMF...or if you could use the "J" and somehow incorporate an artistic drawing/shape of a 'power trowel' (what we use apply a smooth finish to the concrete with) but still visually see that its a J, would be cool. Would like to see designs using Black with silver or grey lettering but are open to other ideas. Seen a business card online with the front of the business card looking like concrete and with just the word CONCRETE on it... On the back was the company name , address and contact info of the company....looked really good! i clicked doubled sided in case of something like that but we are open to just single sided as well. After viewing some of the designs, maybe a pop of colour would be nice ... open to any ideas and colours.😊

Target Market(s)

Construction

```html
<!DOCTYPE html>
<html lang="en">
<head>
<meta charset="utf-8">
<title>H M Ferrick &amp; Sons Ltd. – Business Card</title>
<link href="https://fonts.googleapis.com/css2?family=Montserrat:wght@400;500;600;700&display=swap" rel="stylesheet">
<style>
  :root {
    --brand-red: #a0091f;
    --brand-red-dark: #8a0619;
    --ink: #2b2b2b;
    --paper: #ffffff;
    --stage: #e6e6e6;
  }
  * { margin: 0; padding: 0; box-sizing: border-box; }
  html, body {
    width: 1200px; height: 930px; overflow: hidden;
    background: var(--stage);
    font-family: "Montserrat", sans-serif;
  }
  .sheet { position: relative; width: 1200px; height: 930px; }
  .card {
    position: absolute; left: 250px; width: 700px; height: 400px;
    border-radius: 28px;
    box-shadow: 0 10px 28px rgba(0,0,0,0.22);
    overflow: hidden;
  }
  .card--front { top: 40px; background: var(--brand-red); }
  .card--back { top: 490px; background: var(--paper); }

  .wordmark { position: absolute; display: flex; align-items: center; }
  .wordmark__square { flex: none; }
  .wordmark__name {
    font-weight: 600; text-transform: uppercase; white-space: nowrap;
  }
  .card--front .wordmark { left: 0; right: 0; top: 176px; justify-content: center; gap: 14px; }
  .card--front .wordmark__square { width: 22px; height: 22px; background: var(--paper); }
  .card--front .wordmark__name { color: var(--paper); font-size: 30px; letter-spacing: 1.5px; }

  .card--back .wordmark { left: 40px; width: 290px; top: 188px; gap: 12px; }
  .card--back .wordmark__square { width: 18px; height: 18px; background: var(--brand-red); }
  .card--back .wordmark__name { color: var(--brand-red); font-size: 15px; letter-spacing: 1px; }

  .divider {
    position: absolute; left: 355px; top: 90px; width: 1.5px; height: 220px;
    background: var(--brand-red);
  }
  .contact { position: absolute; left: 385px; top: 92px; color: var(--ink); }
  .contact__name {
    color: var(--brand-red); font-weight: 700; font-size: 27px;
    letter-spacing: 0.5px; text-transform: uppercase; line-height: 1.1;
    white-space: nowrap;
  }
  .contact__title { font-size: 15px; margin: 4px 0 14px; }
  .contact__address { font-size: 14px; line-height: 1.45; margin-bottom: 10px; }
  .contact__list { list-style: none; font-size: 14px; line-height: 1.5; }
  .contact__list li { display: flex; align-items: center; gap: 9px; }
  .contact__icon { width: 13px; height: 13px; flex: none; }
</style>
</head>
<body>
<main class="sheet">
  <section class="card card--front" aria-label="Card front">
    <div class="wordmark">
      <span class="wordmark__square"></span>
      <span class="wordmark__name">H M Ferrick &amp; Sons Ltd.</span>
    </div>
  </section>

  <section class="card card--back" aria-label="Card back">
    <div class="wordmark">
      <span class="wordmark__square"></span>
      <span class="wordmark__name">H M Ferrick &amp; Sons Ltd.</span>
    </div>
    <div class="divider"></div>
    <div class="contact">
      <p class="contact__name">Gerald Parsons</p>
      <p class="contact__title">Founder</p>
      <p class="contact__address">P.O.Box 41, Site 9, RR#2<br>Cedar Harbour, NL A0K 2B0</p>
      <ul class="contact__list">
        <li>
          <svg class="contact__icon" viewBox="0 0 24 24" fill="var(--brand-red)"><path d="M6.6 10.8a15 15 0 0 0 6.6 6.6l2.2-2.2a1 1 0 0 1 1-.25 11.4 11.4 0 0 0 3.6.57 1 1 0 0 1 1 1V20a1 1 0 0 1-1 1A17 17 0 0 1 3 4a1 1 0 0 1 1-1h3.5a1 1 0 0 1 1 1c0 1.25.2 2.45.57 3.57a1 1 0 0 1-.25 1z"/></svg>
          (709) 555-0142
        </li>
        <li>
          <svg class="contact__icon" viewBox="0 0 24 24" fill="var(--brand-red)"><rect x="6" y="2" width="12" height="6"/><rect x="2" y="9" width="20" height="9" rx="2"/><rect x="6" y="15" width="12" height="7"/></svg>
          (709) 555-0187
        </li>
        <li>
          <svg class="contact__icon" viewBox="0 0 24 24" fill="none" stroke="var(--brand-red)" stroke-width="2.2"><rect x="6" y="2" width="12" height="20" rx="2"/><line x1="11" y1="18" x2="13" y2="18"/></svg>
          (709) 555-0163 Home-Res
        </li>
        <li>
          <svg class="contact__icon" viewBox="0 0 24 24" fill="none" stroke="var(--brand-red)" stroke-width="2.2"><rect x="2" y="5" width="20" height="14"/><polyline points="2,5 12,13 22,5"/></svg>
          hm_ferrick@mailbox.com
        </li>
      </ul>
    </div>
  </section>
</main>
</body>
</html>
```